New Wanderly Site!!

Hello everyone!
We're WanderlyTrips. A tour company which offer group excursions to places like Morocco & Portugal for young adults. We have been in the business for 10 years now and we'd like to create a new fresh look and feel design. Something clean and more modern.
We offer trips to:
1 - Weekend trips Lagos, Portugal
2 - Weekend tips to Morocco
3 - 5 day trip to the Sahara Desert in Morocco
4 - Beach day trips to Cadiz
5 - Day trip to Gibraltar
6 - Costume trips
7 - Wine Tasting day trip
8 - Fiestas del Torvell
Those are the 8 boxes we'd like to have on our home-page along with an awesome header and footer. You can take a look for our current page to see sections and the text of the sections. Once we approve a nice home page from any of you designers, we will go ahead and send you the names of all the pages we'd like you to design for us. We already have someone who will code all the pages. We just need a new design for all the pages.
You can see our logo on our Blog: http://wanderlytripsblog.example/
We like websites like:
www.Palorvia.example
www.Skarmet.example
We look forward to hear from you!!
PS:
we will need the home page and other pages.
7 pages plus 8 trip pages. The trip pages they can all look the same (design wise) obviusly diferent photos, video and content. Total 15 pages.
Page 1 - Home page
Page 2 - About us. This page can look similar to:
Page 3 - FAQs. This page can look similar to:
Page 4 - Contact us. This page can look similar to: http://www.palorvia.example/contact
Page 5 - Trip check in. This page can look similar to the Skarmet.example look for flight check in. Something clean.
Page 6 - Trip videos. This page, will have the list of all our trip videos. A line or two of the trip and the video right below.
Page 7 - Trip departure info. On this page we're going to have the information on how to get to Sevilla. Also the google map of the actual meeting point and maybe a youtube video somewhere.
Page 8 - Why travel with us.
How many trip page are we going to need?
We have 8 trips. If you can just do 1 page, then you can do the same type page for all the trips. On each trip page you must add the following content:
Trip overview
Whats included
Trip dates
Photos and a youtube video.
An example of our current lagos trip page is:
https://www.wanderlytrips.example/2001/09/beach-getaway-lagos-portugal/
You can take all the content from www.WanderlyTrips.example

```html
<!DOCTYPE html>
<html lang="en">
<head>
<meta charset="utf-8">
<title>WanderlyTrips – Home</title>
<link href="https://fonts.googleapis.com/css2?family=Open+Sans:ital,wght@0,400;0,600;0,700;1,400&display=swap" rel="stylesheet">
<style>
:root{
  --black:#000;
  --ink:#111;
  --yellow:#fdc533;
  --yellow-deep:#f2a81d;
  --red:#c8101c;
  --gray:#d9d9d9;
  --gray-light:#ececec;
  --footer-dark:#1c1c1c;
  --muted:#8a8a8a;
  --white:#fff;
  --sand:#d6b28c;
}
*{box-sizing:border-box;margin:0;padding:0}
html,body{width:1080px;height:1200px;overflow:hidden;background:var(--white)}
body{font-family:Arial,Helvetica,sans-serif;color:var(--ink)}
.page{position:absolute;left:0;top:0;width:1240px;height:1378px;transform:scale(0.871);transform-origin:0 0;background:var(--white)}
.abs{position:absolute}

/* header */
.brand{left:155px;top:22px;display:flex;align-items:center;gap:10px;font-family:'Open Sans',sans-serif;font-weight:700;font-size:26px;color:var(--ink)}
.brand-dot{width:22px;height:22px;border-radius:50%;background:var(--yellow-deep)}
.account{left:819px;top:0;width:163px;height:33px;background:var(--black);color:var(--white);font-size:14px;display:flex;align-items:center;justify-content:center;gap:12px}
.flag{top:9px;width:34px;height:22px}
.search{left:775px;top:43px;width:302px;height:30px;border:1px solid #bbb}
.search svg{position:absolute;right:6px;top:5px}

/* nav */
.main-nav{left:0;top:96px;width:1240px;height:47px;background:var(--black)}
.main-nav ul{list-style:none;display:flex;position:absolute;left:151px;top:0;height:47px}
.main-nav li{color:var(--white);font-size:14.5px;line-height:47px;padding:0 12px}
.main-nav li.active{background:var(--yellow);color:var(--ink);padding:0 13px}

/* hero */
.hero{left:150px;top:143px;width:939px;height:411px;background:linear-gradient(180deg,#c9a889 0%,#dcc2a4 50%,#cfae8c 100%)}
.booking{left:771px;top:181px;width:288px;height:337px;background:linear-gradient(180deg,var(--yellow) 0%,var(--yellow-deep) 100%);border-radius:0 6px 6px 6px}
.tab{top:186px;height:30px;background:var(--black);color:var(--white);font-size:14px;display:flex;align-items:center;gap:6px;padding:0 8px}
.tab-flight{left:771px;top:181px;width:122px;height:38px;background:var(--yellow);color:#333;font-size:14px;display:flex;align-items:center;justify-content:center;gap:10px}
.opt{font-size:11px;color:#333;display:flex;align-items:center;gap:6px}
.box{width:9px;height:9px;background:var(--white);border:1px solid #ccc}
.field{left:797px;width:239px;height:22px;background:var(--white);border:1px solid #e0c070;font-size:11px;color:#aaa;padding:4px 5px}
.field .r{position:absolute;right:8px;top:4px;color:#333;font-size:9px}
.mini{top:421px;width:67px;height:22px;background:var(--white);font-size:9px;color:#aaa;padding:6px 4px}
.mini .r{position:absolute;right:5px;top:4px;color:#333;font-size:8px;line-height:7px}
.label{left:797px;top:403px;font-size:11px;color:#333}
.search-btn{left:868px;top:466px;width:90px;height:30px;background:var(--red);color:var(--white);font-size:14px;display:flex;align-items:center;justify-content:center;border:1px solid #ffd}

/* featured */
.featured{left:150px;top:571px;width:622px;height:229px;background:var(--gray-light);border:1px solid #ddd}
.feature-img{top:577px;width:299px;height:216px}
.feature-title{font-family:'Open Sans',sans-serif;font-weight:700;color:var(--white)}

/* news */
.news{left:785px;top:571px;width:304px;height:229px;background:var(--gray);border:1px solid #ccc}
.news h2{position:absolute;left:15px;top:8px;font-family:'Open Sans',sans-serif;font-weight:700;font-size:20px;letter-spacing:.5px}
.news-item{left:796px;width:282px;height:86px;background:var(--white)}
.news-thumb{position:absolute;left:4px;top:4px;width:103px;height:78px}
.news-text{position:absolute;left:120px;top:8px;font-family:'Open Sans',sans-serif;font-size:13px;line-height:25px;color:#444;letter-spacing:.4px}
.news-text b{color:var(--ink);font-weight:600}
.news-arrow{position:absolute;right:8px;bottom:6px}

/* trip cards */
.card{width:304px;height:229px;background:var(--black)}
.card-img{position:absolute;left:0;top:0;width:304px;height:158px}
.card h3{position:absolute;left:10px;top:165px;font-family:'Open Sans',sans-serif;font-weight:600;font-size:16px;color:var(--white);letter-spacing:.5px}
.card p{position:absolute;left:10px;top:186px;font-family:'Open Sans',sans-serif;font-style:italic;font-size:11px;line-height:16px;color:var(--white);letter-spacing:.5px}
.more{position:absolute;right:0;bottom:0;width:94px;height:24px;background:var(--yellow);font-family:'Open Sans',sans-serif;font-size:11.5px;color:#222;display:flex;align-items:center;justify-content:center;gap:6px;letter-spacing:.4px}

/* footer */
.foot-nav{left:0;top:1305px;width:1240px;height:36px;background:var(--black)}
.foot-nav ul{list-style:none;display:flex;position:absolute;left:148px;top:0}
.foot-nav li{color:var(--white);font-size:11px;line-height:38px;padding:0 9.5px}
.subscribe{left:903px;top:1314px;width:164px;height:20px;background:var(--white);font-family:'Open Sans',sans-serif;font-size:11px;color:#999;padding:2px 8px;letter-spacing:.4px}
.go{left:1068px;top:1314px;width:22px;height:20px;background:var(--yellow-deep);font-size:11px;font-weight:700;text-align:center;line-height:20px}
.foot-base{left:0;top:1341px;width:1240px;height:37px;background:var(--footer-dark)}
.copy{left:160px;top:1351px;font-family:'Open Sans',sans-serif;font-size:10.5px;color:var(--muted);letter-spacing:.6px}
.social{top:1350px;width:16px;height:16px;border-radius:3px}
</style>
</head>
<body>
<div class="page">

  <header>
    <div class="abs brand"><span class="brand-dot"></span>WanderlyTrips</div>
    <div class="abs account"><span>Login</span><span>|</span><span>Register</span></div>
    <svg class="abs flag" style="left:1000px" viewBox="0 0 34 22" aria-label="Spanish"><rect width="34" height="22" fill="#c60b1e"/><rect y="5.5" width="34" height="11" fill="#ffc400"/></svg>
    <svg class="abs flag" style="left:1043px" viewBox="0 0 34 22" aria-label="English"><rect width="34" height="22" fill="#012169"/><path d="M0 0L34 22M34 0L0 22" stroke="#fff" stroke-width="4"/><path d="M0 0L34 22M34 0L0 22" stroke="#c8102e" stroke-width="1.5"/><path d="M17 0V22M0 11H34" stroke="#fff" stroke-width="6"/><path d="M17 0V22M0 11H34" stroke="#c8102e" stroke-width="3.5"/></svg>
    <div class="abs search"><svg width="20" height="20" viewBox="0 0 20 20"><circle cx="8" cy="8" r="6" fill="none" stroke="#333" stroke-width="2"/><path d="M12.5 12.5L18 18" stroke="#333" stroke-width="2.5"/></svg></div>
  </header>

  <nav class="abs main-nav">
    <ul>
      <li class="active">Home</li><li>About Us</li><li>Excursions</li><li>Group Bookings</li><li>Morocco &amp; The Sahara Desert</li><li>Why Travel With Us?</li><li>Trip Videos</li><li>Contact Us</li>
    </ul>
  </nav>

  <section>
    <div class="abs hero" role="img" aria-label="Photo: camels led by a guide across desert sand dunes"></div>
    <div class="abs booking"></div>
    <div class="abs tab-flight"><svg width="20" height="20" viewBox="0 0 20 20"><path d="M10 1L11.5 8L19 11V12.5L11.5 11L11 16L13 17.5V19L10 18L7 19V17.5L9 16L8.5 11L1 12.5V11L8.5 8Z" fill="#333"/></svg>Flight</div>
    <div class="abs tab" style="left:895px;width:81px;"><svg width="18" height="14" viewBox="0 0 18 14"><path d="M2 5H13V9A4 4 0 0 1 9 13H6A4 4 0 0 1 2 9Z M13 6H15A2 2 0 0 1 15 10H13" fill="#fff" stroke="#fff"/></svg>Hotels</div>
    <div class="abs tab" style="left:979px;width:74px;"><svg width="22" height="16" viewBox="0 0 22 16"><path d="M4 7L6 2H16L18 7H20V13H2V7Z" fill="none" stroke="#fff" stroke-width="1.6"/><circle cx="6" cy="13" r="2" fill="#fff"/><circle cx="16" cy="13" r="2" fill="#fff"/></svg>Cars</div>
    <div class="abs opt" style="left:798px;top:235px"><span class="box" style="background:#fff;box-shadow:inset 0 0 0 2px #fff,inset 0 0 0 5px #555"></span>Round Trip</div>
    <div class="abs opt" style="left:900px;top:235px"><span class="box"></span>One way</div>
    <div class="abs field" style="top:266px">Portugal<span class="r">▼</span></div>
    <div class="abs field" style="top:299px">Destination<span class="r">▼</span></div>
    <div class="abs field" style="top:337px">From<svg class="r" style="top:4px" width="13" height="13" viewBox="0 0 13 13"><rect x=".5" y="1.5" width="12" height="11" fill="none" stroke="#555"/><path d="M1 4H12M3 7H10M3 9.5H10M5 4V12M8 4V12" stroke="#555"/></svg></div>
    <div class="abs field" style="top:370px">To<svg class="r" style="top:4px" width="13" height="13" viewBox="0 0 13 13"><rect x=".5" y="1.5" width="12" height="11" fill="none" stroke="#555"/><path d="M1 4H12M3 7H10M3 9.5H10M5 4V12M8 4V12" stroke="#555"/></svg></div>
    <div class="abs label">Number of passengers</div>
    <div class="abs mini" style="left:798px">1 Adult<span class="r">▲<br>▼</span></div>
    <div class="abs mini" style="left:884px">1 Children<span class="r">▲<br>▼</span></div>
    <div class="abs mini" style="left:969px">0 babies<span class="r">▲<br>▼</span></div>
    <div class="abs search-btn">Search Now</div>
  </section>

  <section>
    <div class="abs featured"></div>
    <div class="abs feature-img" style="left:157px;background:linear-gradient(180deg,#9a7042 0%,#c46f12 45%,#c86a0c 100%)" role="img" aria-label="Photo: camel caravan crossing Sahara dunes at sunset"></div>
    <div class="abs feature-title" style="left:178px;top:700px;font-size:33px">5 day trip to the</div>
    <div class="abs feature-title" style="left:178px;top:742px;font-size:21px">Sahara Desert in Morocco</div>
    <div class="abs feature-img" style="left:467px;background:linear-gradient(180deg,#bcd7e6 0%,#8fb1c6 50%,#4f7b98 100%)" role="img" aria-label="Photo: domed seaside pavilion on the beach at Cadiz"></div>
    <div class="abs feature-title" style="left:485px;top:694px;font-size:30px;line-height:36px">Beach day trips to<br>Cadiz</div>

    <aside class="abs news">
      <h2>Latest News</h2>
    </aside>
    <div class="abs news-item" style="top:615px">
      <div class="news-thumb" style="background:linear-gradient(180deg,#3d2a3a 0%,#b2573a 50%,#1ab0d2 100%)" role="img" aria-label="Photo: resort pool at dusk"></div>
      <div class="news-text"><b>Lorium ipsum</b><br>consectetur adipisicing<br>elit, sed do</div>
      <svg class="news-arrow" width="16" height="12" viewBox="0 0 16 12"><path d="M1 6H14M9 1L14 6L9 11" fill="none" stroke="#f2a81d" stroke-width="2.2"/></svg>
    </div>
    <div class="abs news-item" style="top:704px">
      <div class="news-thumb" style="background:linear-gradient(180deg,#6aa2d8 0%,#9c8a6a 50%,#1fa3c7 100%)" role="img" aria-label="Photo: hotel swimming pool with palm trees"></div>
      <div class="news-text"><b>Lorium ipsum</b><br>consectetur adipisicing<br>elit, sed do</div>
      <svg class="news-arrow" width="16" height="12" viewBox="0 0 16 12"><path d="M1 6H14M9 1L14 6L9 11" fill="none" stroke="#f2a81d" stroke-width="2.2"/></svg>
    </div>
  </section>

  <section>
    <article class="abs card" style="left:150px;top:821px">
      <div class="card-img" style="background:linear-gradient(180deg,#8ea7c4 0%,#7d7a70 60%,#9aa6b4 100%)" role="img" aria-label="Photo: Rock of Gibraltar seen from a promenade"></div>
      <h3>Day trip to Gibraltar</h3><p>Lorem Ipsum is simply dummy<br>text of the printing</p>
      <div class="more">view more <svg width="14" height="10" viewBox="0 0 14 10"><path d="M1 5H12M8 1L12 5L8 9" fill="none" stroke="#222" stroke-width="1.8"/></svg></div>
    </article>
    <article class="abs card" style="left:468px;top:821px">
      <div class="card-img" style="background:linear-gradient(120deg,#1f8fb4 0%,#2bb0a8 45%,#c7a05e 75%,#d8c49a 100%)" role="img" aria-label="Photo: rocky coves and turquoise water at Lagos"></div>
      <h3>Weekend trips Lagos, Portugal</h3><p>Lorem Ipsum is simply dummy<br>text of the printing</p>
      <div class="more">view more <svg width="14" height="10" viewBox="0 0 14 10"><path d="M1 5H12M8 1L12 5L8 9" fill="none" stroke="#222" stroke-width="1.8"/></svg></div>
    </article>
    <article class="abs card" style="left:785px;top:821px">
      <div class="card-img" style="background:linear-gradient(180deg,#c08a5c 0%,#d9a676 55%,#b9875a 100%)" role="img" aria-label="Photo: riders on camels crossing desert dunes"></div>
      <h3>Weekend tips to Morocco</h3><p>Lorem Ipsum is simply dummy<br>text of the printing</p>
      <div class="more">view more <svg width="14" height="10" viewBox="0 0 14 10"><path d="M1 5H12M8 1L12 5L8 9" fill="none" stroke="#222" stroke-width="1.8"/></svg></div>
    </article>
    <article class="abs card" style="left:150px;top:1064px">
      <div class="card-img" style="background:linear-gradient(180deg,#5fa6cf 0%,#3a7a98 60%,#d9e4ea 100%)" role="img" aria-label="Photo: surfer in costume riding a wave"></div>
      <h3>Costume trips</h3><p>Lorem Ipsum is simply dummy<br>text of the printing</p>
      <div class="more">view more <svg width="14" height="10" viewBox="0 0 14 10"><path d="M1 5H12M8 1L12 5L8 9" fill="none" stroke="#222" stroke-width="1.8"/></svg></div>
    </article>
    <article class="abs card" style="left:468px;top:1064px">
      <div class="card-img" style="background:linear-gradient(180deg,#3a2b20 0%,#8a7a5c 50%,#c8b98a 100%)" role="img" aria-label="Photo: glasses of white wine"></div>
      <h3>Wine Tasting day trip</h3><p>Lorem Ipsum is simply dummy<br>text of the printing</p>
      <div class="more">view more <svg width="14" height="10" viewBox="0 0 14 10"><path d="M1 5H12M8 1L12 5L8 9" fill="none" stroke="#222" stroke-width="1.8"/></svg></div>
    </article>
    <article class="abs card" style="left:785px;top:1064px">
      <div class="card-img" style="background:linear-gradient(180deg,#b8873f 0%,#8a6a42 55%,#c8b392 100%)" role="img" aria-label="Photo: horseback riders on a beach at sunset"></div>
      <h3>Horseback riding trip</h3><p>Lorem Ipsum is simply dummy<br>text of the printing</p>
      <div class="more">view more <svg width="14" height="10" viewBox="0 0 14 10"><path d="M1 5H12M8 1L12 5L8 9" fill="none" stroke="#222" stroke-width="1.8"/></svg></div>
    </article>
  </section>

  <footer>
    <nav class="abs foot-nav">
      <ul><li>Home</li><li>About Us</li><li>Excursions</li><li>Group Bookings</li><li>Morocco &amp; The Sahara Desert</li><li>Why Travel With Us?</li><li>Trip Videos</li><li>Contact Us</li></ul>
    </nav>
    <div class="abs subscribe">Enter your email id</div>
    <div class="abs go">Go</div>
    <div class="abs foot-base"></div>
    <div class="abs copy">© 2013 wanderlytrips - Terms of Service - Privacy Policy - Program Policies</div>
    <div class="abs social" style="left:1027px;background:#4aa3df"></div>
    <div class="abs social" style="left:1049px;background:#f28a1d"></div>
    <div class="abs social" style="left:1071px;background:#3b5b9a"></div>
  </footer>

</div>
</body>
</html>
```